Corvell Lending Partners. Professional and Established Company

A full service finance company specializing in obtaining capital for small business. Business Lending advisor, helping small business owners access the capital they need to launch, grow, or sustain their business. Many of our programs offer flexible guidelines to overcome common obstacles such as credit score, credit history, and time in business, financials, and industry type. Our streamlined funding process makes getting a business loan, business line of credit, stated income commercial real estate loan, a smooth and stress free experience.SOME OF THE MOST COMMON NEEDS FOR BUSINESS CAPITAL:• Working Capital• Debt Consolidations (loans, merchant cash advances, etc.)• Payroll• Operating Expenses• Inventory• Equipment Financing• Commercial Real Estate (Purchase, Fix & Flip, Rehab, Renovations)• Business Acquisitions• Business ExpansionWe like the websites:www.brandtwoodfc.com they are in the same industry and provide the same servicesWe are wanting to be able to update when we do press releases and such using Word Press. Our look should be very professional and we will be adding Our Team Professional Bios and Headshots.

Industry/Entity Type

Finance

Number of Pages Required

5+ page

Font styles to use
Serif
Sans Serif

Requirements
Must have
• We want to copy brandtwoodfc.com
• We need:
• Home Page
• About Us
• Loan Programs
• Loan Criteria
• News
• Apply Now
• Contact
Nice to have
• See brandtwoodfc.com
Should not have
• Need professional design. Nothing bright or abstract

```html
<!DOCTYPE html>
<html lang="en">
<head>
<meta charset="utf-8">
<title>Corvell Lending Partners</title>
<link href="https://fonts.googleapis.com/css2?family=Roboto:wght@400;500;700&family=Open+Sans:wght@400;600&family=Poppins:wght@500;600&display=swap" rel="stylesheet">
<style>
:root{
  --blue:#1a55ad;
  --blue-deep:#124a9c;
  --green:#1a9a4c;
  --money:#2fc46e;
  --ink:#1d1d1d;
  --text:#444;
  --muted:#666;
  --line:#c9c9c9;
  --header:#fdf5f3;
  --team-bg:#efefef;
}
*{box-sizing:border-box;margin:0;padding:0}
html,body{width:1200px;height:4082px;overflow:hidden}
body{font-family:"Open Sans",Arial,sans-serif;color:var(--text);background:#fff;position:relative}
a{color:inherit;text-decoration:none}
section,header,footer{position:relative;width:1200px}

/* header */
.site-header{height:122px;background:var(--header)}
.logo{position:absolute;left:144px;top:36px;font-family:"Roboto",Arial,sans-serif;font-weight:700;font-size:30px;color:var(--blue);letter-spacing:.5px}
.contact-top{position:absolute;right:366px;top:14px;text-align:right;font-family:"Roboto",Arial,sans-serif;white-space:nowrap}
.contact-top small{display:block;font-size:16px;line-height:20px;color:#444}
.contact-top strong{display:block;font-size:26px;line-height:30px;font-weight:500;color:var(--ink)}
.phone-badge{position:absolute;left:848px;top:20px;width:40px;height:40px;border-radius:50%;background:#cfcfcf}
.phone-badge svg{position:absolute;left:10px;top:10px}
.btn-apply-top{position:absolute;left:911px;top:20px;width:142px;height:38px;border:2px solid var(--blue);border-radius:20px;font-family:"Roboto",Arial,sans-serif;font-weight:500;font-size:18px;color:var(--ink);display:flex;align-items:center;justify-content:center}
.main-nav{position:absolute;right:146px;top:82px;display:flex;gap:22px;font-family:"Roboto",Arial,sans-serif;font-weight:500;font-size:16px;color:var(--ink)}

/* hero */
.hero{height:653px;background:linear-gradient(180deg,#3a3733 0%,#57514a 45%,#3b3834 100%);overflow:hidden}
.hero-photo{position:absolute;inset:0;background:radial-gradient(ellipse at 55% 35%,rgba(170,150,125,.45),transparent 60%),linear-gradient(90deg,rgba(25,25,25,.55),rgba(60,55,50,.2) 50%,rgba(25,25,25,.55))}
.hero-title{position:absolute;left:0;right:0;top:220px;text-align:center;color:#fff;font-family:"Roboto",Arial,sans-serif}
.hero-title .t1{display:block;font-size:46px;font-weight:400;letter-spacing:1px}
.hero-title .t2{display:block;font-size:56px;font-weight:700;margin-top:-2px}
.btn-hero{position:absolute;left:506px;top:368px;width:186px;height:40px;background:var(--blue);border-radius:22px;color:#fff;font-family:"Roboto",Arial,sans-serif;font-weight:500;font-size:18px;display:flex;align-items:center;justify-content:center}
.arrow{position:absolute;top:288px}
.arrow.prev{left:114px}.arrow.next{left:1064px}
.deals{position:absolute;top:520px;left:0;right:0}
.deal{position:absolute;width:200px;margin-left:-100px;text-align:center;color:#fff}
.deal h4{font-family:"Roboto",Arial,sans-serif;font-weight:500;font-size:15px}
.deal .amount{font-family:"Roboto",Arial,sans-serif;font-size:24px;color:var(--money);margin:4px 0 2px}
.deal p{font-size:11px;line-height:16px}

/* welcome */
.welcome{height:449px;text-align:center}
.section-title{font-family:"Roboto",Arial,sans-serif;font-weight:700;font-size:38px;color:var(--ink)}
.welcome .section-title{position:absolute;left:0;right:0;top:84px}
.welcome .section-title span{color:var(--blue)}
.welcome p{position:absolute;left:175px;width:850px;top:154px;font-size:14px;line-height:32px;color:#444}
.btn-outline{position:absolute;height:38px;border:2px solid var(--blue);border-radius:20px;font-family:"Roboto",Arial,sans-serif;font-weight:500;font-size:17px;color:var(--blue);display:flex;align-items:center;justify-content:center}
.welcome .btn-outline{left:528px;top:310px;width:141px}

/* features */
.feature-row{height:405px;display:flex}
.feature-row .photo{width:604px;height:405px}
.feature-row .panel{width:596px;height:405px;position:relative;color:#fff}
.panel.green{background:linear-gradient(135deg,#1fa553,#158c43)}
.panel.blue{background:linear-gradient(135deg,#1d5bb5,#124793)}
.panel h2{position:absolute;top:88px;font-family:"Roboto",Arial,sans-serif;font-weight:700;font-size:31px}
.panel p{position:absolute;top:148px;width:400px;font-size:14px;line-height:28px}
.panel .btn-ghost{position:absolute;top:288px;width:126px;height:36px;border:2px solid #fff;border-radius:20px;font-family:"Roboto",Arial,sans-serif;font-weight:500;font-size:16px;display:flex;align-items:center;justify-content:center}
.panel.green h2,.panel.green p,.panel.green .btn-ghost{left:60px}
.panel.blue h2,.panel.blue p,.panel.blue .btn-ghost{left:144px}
.photo.meeting{background:linear-gradient(135deg,#3a2c20,#8a6a48 45%,#d9cfc0 75%,#6b5845)}
.photo.office{background:linear-gradient(160deg,#b8bcc2,#5c6470 45%,#2a2f37)}

/* services */
.services{height:1128px}
.services .section-title{position:absolute;left:0;right:0;top:100px;text-align:center}
.service{position:absolute;width:290px}
.service .icon{width:98px;height:98px;border-radius:50%;border:2px solid var(--line);display:flex;align-items:center;justify-content:center;background:#fff}
.service .icon.active{background:var(--blue);border-color:var(--blue)}
.service h3{margin-top:30px;font-family:"Roboto",Arial,sans-serif;font-weight:500;font-size:17px;color:var(--ink)}
.service p{margin-top:12px;font-size:13px;line-height:25px;color:#444}

/* team */
.team{height:623px;background:var(--team-bg)}
.team .section-title{position:absolute;left:0;right:0;top:70px;text-align:center}
.member{position:absolute;top:161px;width:277px;text-align:center}
.member .headshot{width:277px;height:245px;background:linear-gradient(180deg,#e4e6e9 0%,#b7bcc3 55%,#2b3442 100%);box-shadow:0 10px 24px rgba(26,85,173,.18)}
.member .badge{position:absolute;right:8px;top:218px;width:40px;height:40px;border-radius:50%;background:var(--blue);border:3px solid #fff}
.member h3{margin-top:24px;font-family:"Poppins",Arial,sans-serif;font-weight:600;font-size:21px;color:var(--ink)}
.member p{margin:14px auto 0;width:265px;font-size:12.5px;line-height:25px;color:#444}

/* footer */
.site-footer{height:296px;text-align:center;font-size:16px;color:var(--ink)}
.footer-contact{position:absolute;left:0;right:0;top:62px;display:flex;justify-content:center;gap:28px;align-items:center}
.footer-contact span{display:flex;align-items:center;gap:10px}
.footer-links{position:absolute;left:0;right:0;top:106px}
.footer-links a{margin:0 8px}
.copyright{position:absolute;left:0;right:0;top:153px}
.social{position:absolute;top:205px;left:546px;display:flex;gap:13px}
.social span{width:28px;height:28px;border-radius:50%;border:1.5px solid var(--blue)}
.social span.alt{border-color:#c8202a}
</style>
</head>
<body>

<header class="site-header">
  <div class="logo">Corvell Lending Partners</div>
  <div class="contact-top">
    <small>Have any Question?</small>
    <strong>+888 5120 7391</strong>
  </div>
  <div class="phone-badge"><svg width="20" height="20" viewBox="0 0 24 24"><path fill="#fff" d="M6.6 10.8a15.1 15.1 0 0 0 6.6 6.6l2.2-2.2c.3-.3.7-.4 1-.2 1.1.4 2.3.6 3.6.6.6 0 1 .4 1 1V20c0 .6-.4 1-1 1A17 17 0 0 1 3 4c0-.6.4-1 1-1h3.5c.6 0 1 .4 1 1 0 1.3.2 2.5.6 3.6.1.3 0 .7-.2 1z"/></svg></div>
  <a class="btn-apply-top" href="#">Apply Now</a>
  <nav class="main-nav">
    <a href="#">HOME</a><a href="#">ABOUT US</a><a href="#">LOAN PROGRAMS</a><a href="#">LOAN CRITERIA</a><a href="#">NEWS</a><a href="#">CONTACT</a>
  </nav>
</header>

<section class="hero">
  <div class="hero-photo" role="img" aria-label="Business advisor smiling with clients in a bright office"></div>
  <h1 class="hero-title"><span class="t1">CORVELL BUSINESS</span><span class="t2">LENDING ADVISOR</span></h1>
  <a class="btn-hero" href="#">APPLY NOW</a>
  <svg class="arrow prev" width="22" height="22" viewBox="0 0 22 22"><path d="M14 4l-7 7 7 7" fill="none" stroke="#fff" stroke-width="3"/></svg>
  <svg class="arrow next" width="22" height="22" viewBox="0 0 22 22"><path d="M8 4l7 7-7 7" fill="none" stroke="#fff" stroke-width="3"/></svg>
  <div class="deals">
    <div class="deal" style="left:212px"><h4>Mixed-use</h4><div class="amount">$21,000,000</div><p>Refinancing &amp; Debt payoff<br>Lake City, MI</p></div>
    <div class="deal" style="left:405px"><h4>Mixed-use</h4><div class="amount">$3,250,000</div><p>Refinancing &amp; Debt payoff<br>Lake City, MI</p></div>
    <div class="deal" style="left:598px"><h4>Mixed-use</h4><div class="amount">$21,000,000</div><p>Refinancing &amp; Debt payoff<br>Lake City, MI</p></div>
    <div class="deal" style="left:792px"><h4>Mixed-use</h4><div class="amount">$4,000,000</div><p>Refinancing &amp; Debt payoff<br>Lake City, MI</p></div>
    <div class="deal" style="left:987px"><h4>Mixed-use</h4><div class="amount">$21,000,000</div><p>Refinancing &amp; Debt payoff<br>Lake City, MI</p></div>
  </div>
</section>

<section class="welcome">
  <h2 class="section-title">WELCOME TO <span>CORVELL</span></h2>
  <p>Lorem ipsum dolor sit amet, consectetur adipiscing elit, sed do eiusmod tempor incididunt ut labore et dolore magna aliqua. Ut enim ad minim veniam, quis nostrud exercitation ullamco laboris nisi ut aliquip ex ea commodo consequat. Duis aute irure dolor in reprehenderit in voluptate velit esse cillum dolore eu fugiat nulla pariatur. Excepteur sint occaecat cupidatat non proident, sunt in culpa qui officia deserunt mollit anim id est laborum</p>
  <a class="btn-outline" href="#">READ MORE</a>
</section>

<section class="feature-row">
  <div class="photo meeting" role="img" aria-label="Advisors reviewing financial charts at a table"></div>
  <div class="panel green">
    <h2>LOAN PROGRAMS</h2>
    <p>Sed ut perspiciatis unde omnis iste natus error sit vitatem aantium doloremque laudantium, totam rem aperiam, eaque ipsa quae ab illo inventore veritatis et quasi arc-tecto beatae vitae dicta sunt explibo.</p>
    <a class="btn-ghost" href="#">READ MORE</a>
  </div>
</section>
<section class="feature-row">
  <div class="panel blue">
    <h2>RECENT NEWS</h2>
    <p>Sed ut perspiciatis unde omnis iste natus error sit vitatem aantium doloremque laudantium, totam rem aperiam, eaque ipsa quae ab illo inventore veritatis et quasi arc-tecto beatae vitae dicta sunt explibo.</p>
    <a class="btn-ghost" href="#">READ MORE</a>
  </div>
  <div class="photo office" role="img" aria-label="Presenter in a trading office with monitors and sales figures"></div>
</section>

<section class="services">
  <h2 class="section-title">OUR SERVICES</h2>

  <div class="service" style="left:144px;top:229px">
    <div class="icon active"><svg width="50" height="50" viewBox="0 0 50 50" fill="none" stroke="#fff" stroke-width="2"><circle cx="25" cy="25" r="9"/><circle cx="25" cy="25" r="17" stroke-dasharray="6 4"/></svg></div>
    <h3>WORKING CAPITAL</h3>
    <p>Lorem ipsum dolor sit amet, consectetur adipiscing elit, sed do eiusmod tempor incididunt ut labore et dolore elit, sed do eiusmod tempor incididunt</p>
  </div>
  <div class="service" style="left:476px;top:229px">
    <div class="icon"><svg width="50" height="50" viewBox="0 0 50 50" fill="none" stroke="var(--blue)" stroke-width="2"><rect x="12" y="8" width="26" height="34" rx="2"/><path d="M17 16h16M17 22h16M17 28h10"/></svg></div>
    <h3>DEBT CONSOLIDATIONS</h3>
    <p>Lorem ipsum dolor sit amet, consectetur adipiscing elit, sed do eiusmod tempor incididunt ut labore et dolore elit, sed do eiusmod tempor incididunt</p>
  </div>
  <div class="service" style="left:808px;top:229px">
    <div class="icon"><svg width="50" height="50" viewBox="0 0 50 50" fill="none" stroke="var(--blue)" stroke-width="2"><rect x="14" y="8" width="22" height="34" rx="2"/><circle cx="25" cy="30" r="5"/><path d="M19 15h12M19 20h12"/></svg></div>
    <h3>PAYROLL</h3>
    <p>Lorem ipsum dolor sit amet, consectetur adipiscing elit, sed do eiusmod tempor incididunt ut labore et dolore elit, sed do eiusmod tempor incididunt</p>
  </div>

  <div class="service" style="left:144px;top:516px">
    <div class="icon"><svg width="50" height="50" viewBox="0 0 50 50" fill="none" stroke="var(--blue)" stroke-width="2"><rect x="9" y="12" width="32" height="22" rx="2"/><path d="M14 29l7-7 5 4 9-9M19 40h12M25 34v6"/></svg></div>
    <h3>OPERATING EXPENSES</h3>
    <p>Lorem ipsum dolor sit amet, consectetur adipiscing elit, sed do eiusmod tempor incididunt ut labore et dolore elit, sed do eiusmod tempor incididunt</p>
  </div>
  <div class="service" style="left:476px;top:516px">
    <div class="icon"><svg width="50" height="50" viewBox="0 0 50 50" fill="none" stroke="var(--blue)" stroke-width="2"><rect x="10" y="20" width="14" height="14"/><rect x="26" y="20" width="14" height="14"/><rect x="18" y="6" width="14" height="14"/><path d="M8 40h34"/></svg></div>
    <h3>INVENTORY</h3>
    <p>Lorem ipsum dolor sit amet, consectetur adipiscing elit, sed do eiusmod tempor incididunt ut labore et dolore elit, sed do eiusmod tempor incididunt</p>
  </div>
  <div class="service" style="left:808px;top:516px">
    <div class="icon"><svg width="50" height="50" viewBox="0 0 50 50" fill="none" stroke="var(--blue)" stroke-width="2"><path d="M9 40h32M13 40V28h10v12M27 40V18h10v22M16 18l8-8 5 5"/></svg></div>
    <h3>EQUIPMENT FINANCING</h3>
    <p>Lorem ipsum dolor sit amet, consectetur adipiscing elit, sed do eiusmod tempor incididunt ut labore et dolore elit, sed do eiusmod tempor incididunt</p>
  </div>

  <div class="service" style="left:144px;top:804px">
    <div class="icon"><svg width="50" height="50" viewBox="0 0 50 50" fill="none" stroke="var(--blue)" stroke-width="2"><rect x="12" y="10" width="14" height="32"/><rect x="26" y="18" width="12" height="24"/><path d="M16 16h6M16 22h6M16 28h6M30 24h4M30 30h4M8 42h34"/></svg></div>
    <h3>COMMERCIAL REAL ESTATE</h3>
    <p>Lorem ipsum dolor sit amet, consectetur adipiscing elit, sed do eiusmod tempor incididunt ut labore et dolore elit, sed do eiusmod tempor incididunt</p>
  </div>
  <div class="service" style="left:476px;top:804px">
    <div class="icon"><svg width="50" height="50" viewBox="0 0 50 50" fill="none" stroke="var(--blue)" stroke-width="2"><circle cx="25" cy="19" r="9"/><path d="M18 26l-4 16 11-5 11 5-4-16"/></svg></div>
    <h3>BUSINESS ACQUISITIONS</h3>
    <p>Lorem ipsum dolor sit amet, consectetur adipiscing elit, sed do eiusmod tempor incididunt ut labore et dolore elit, sed do eiusmod tempor incididunt</p>
  </div>
  <div class="service" style="left:808px;top:804px">
    <div class="icon"><svg width="50" height="50" viewBox="0 0 50 50" fill="none" stroke="var(--blue)" stroke-width="2"><rect x="10" y="14" width="30" height="20" rx="2"/><path d="M15 29l6-6 5 4 8-8M20 34v6M30 34v6M16 40h18"/></svg></div>
    <h3>BUSINESS EXPANSION</h3>
    <p>Lorem ipsum dolor sit amet, consectetur adipiscing elit, sed do eiusmod tempor incididunt ut labore et dolore elit, sed do eiusmod tempor incididunt</p>
  </div>
</section>

<section class="team">
  <h2 class="section-title">OUR TEAM</h2>
  <div class="member" style="left:144px">
    <div class="headshot" role="img" aria-label="Headshot of team member Owen Hartley"></div>
    <span class="badge"></span>
    <h3>Owen Hartley</h3>
    <p>Sed ut perspiciatis unde omnis iste natus error sit voluptatem accusantium dolque laudantium, totam rem aperiam</p>
  </div>
  <div class="member" style="left:462px">
    <div class="headshot" role="img" aria-label="Headshot of team member Marcus Reyes"></div>
    <span class="badge"></span>
    <h3>Marcus Reyes</h3>
    <p>Sed ut perspiciatis unde omnis iste natus error sit voluptatem accusantium dolque laudantium, totam rem aperiam</p>
  </div>
  <div class="member" style="left:778px">
    <div class="headshot" role="img" aria-label="Headshot of team member Daniel Ashford"></div>
    <span class="badge"></span>
    <h3>Daniel Ashford</h3>
    <p>Sed ut perspiciatis unde omnis iste natus error sit voluptatem accusantium dolque laudantium, totam rem aperiam</p>
  </div>
</section>

<footer class="site-footer">
  <div class="footer-contact">
    <span><svg width="16" height="16" viewBox="0 0 24 24"><path fill="var(--blue)" d="M6.6 10.8a15.1 15.1 0 0 0 6.6 6.6l2.2-2.2c.3-.3.7-.4 1-.2 1.1.4 2.3.6 3.6.6.6 0 1 .4 1 1V20c0 .6-.4 1-1 1A17 17 0 0 1 3 4c0-.6.4-1 1-1h3.5c.6 0 1 .4 1 1 0 1.3.2 2.5.6 3.6.1.3 0 .7-.2 1z"/></svg>999 3170 6284,</span>
    <span><svg width="14" height="18" viewBox="0 0 14 18"><path fill="var(--blue)" d="M7 0a7 7 0 0 0-7 7c0 5 7 11 7 11s7-6 7-11a7 7 0 0 0-7-7zm0 9.5A2.5 2.5 0 1 1 7 4.5a2.5 2.5 0 0 1 0 5z"/></svg>Suite 14, 5th Floor, PO Box – 4820,</span>
    <span><svg width="18" height="14" viewBox="0 0 18 14" fill="none" stroke="var(--blue)" stroke-width="1.6"><rect x="1" y="1" width="16" height="12" rx="1"/><path d="M1 2l8 6 8-6"/></svg>info@corvelllending.com</span>
  </div>
  <nav class="footer-links">
    <a href="#">Home</a>|<a href="#">About Us</a>|<a href="#">Loan Programs</a>|<a href="#">Loan Criteria</a>|<a href="#">News</a>|<a href="#">Apply Now</a>|<a href="#">Contact</a>
  </nav>
  <p class="copyright">Corvell © 2018 All Rights Reserved.</p>
  <div class="social"><span></span><span></span><span class="alt"></span></div>
</footer>

</body>
</html>
```